Toothbrush Packaging - Colorful Double Pack With Tongue Cleaner

I would like to make a colorful creative packaging for toothbrushes. I want the design to pop off the shelf with color. Something you wont be able to miss.
I like the use of colors to match my logo and flow with the design of package. Also you can be as open and creative as you like since I want the product to stand out. All info and ideas attached in file :)

Target Market(s)

Oral Health

Industry/Entity Type

Retail

Font styles to use
Serif
Sans Serif
Decorative
Script

Requirements
Must have
• 1. Use of colors on packaging
• 2. Logo flows with design color (Do Not Change Or Edit Shape Of Logo since many products are established already with the existing logo design)
• 3. Toothbrush colors are bright neon so make the product & the package colors compliment each other
• 4. Packaging will be similar to the double pack (Luma T 1) Pictures in File
• 5. Make It Look awesome :)
Nice to have
• I do not have a specified size for packaging. So designers can be creative in package design once it is reasonable, eye catching & cool.
Should not have
• Cant say at the moment but I will know along the way :)

```html
<!DOCTYPE html>
<html lang="en">
<head>
<meta charset="utf-8">
<title>Fresh Package – Blister Card</title>
<link href="https://fonts.googleapis.com/css2?family=Poppins:wght@300;600&display=swap" rel="stylesheet">
<style>
  :root {
    --page-bg: #e9e6e1;
    --magenta: #d9509e;
    --pink: #f07ab8;
    --sun: #ffd23a;
    --orange: #f6a42a;
    --sky: #23a3dc;
    --lime: #c3dc3a;
    --white: #ffffff;
    --navy: #0f1a3a;
    --teal: #63c7cc;
    --coral: #ef4e38;
    --violet: #6a35a6;
    --ink: #2b2b3a;
  }
  html, body {
    margin: 0;
    width: 1200px;
    height: 900px;
    overflow: hidden;
    background: var(--page-bg);
  }
  .canvas {
    position: relative;
    width: 1200px;
    height: 900px;
  }
  .blister-card {
    position: absolute;
    left: 406px;
    top: 54px;
    width: 330px;
    height: 748px;
    border-radius: 22px;
    overflow: hidden;
    background:
      linear-gradient(160deg, var(--magenta) 0%, var(--pink) 18%, var(--sun) 34%, var(--sky) 52%, var(--lime) 70%, var(--orange) 86%, var(--magenta) 100%);
  }
  .card-swoosh {
    position: absolute;
    inset: 0;
  }
  .hang-hole {
    position: absolute;
    left: 114px;
    top: 30px;
    width: 100px;
    height: 22px;
    border-radius: 8px;
    background: var(--page-bg);
  }
  .brand {
    position: absolute;
    left: 24px;
    top: 112px;
    display: flex;
    align-items: center;
    gap: 6px;
  }
  .brand-dot {
    width: 14px;
    height: 14px;
    border-radius: 50%;
    background: var(--navy);
  }
  .brand-name {
    font-family: "Poppins", sans-serif;
    font-weight: 600;
    font-size: 17px;
    color: var(--navy);
  }
  .product {
    position: absolute;
    border-radius: 14px;
  }
  .tongue-cleaner {
    left: 74px;
    top: 258px;
    width: 30px;
    height: 444px;
    border-radius: 16px 16px 10px 10px;
    background: linear-gradient(180deg, #ffffff 0%, #b9a6e0 18%, var(--violet) 40%, var(--violet) 100%);
  }
  .brush-teal {
    left: 150px;
    top: 74px;
    width: 70px;
    height: 632px;
    background: linear-gradient(180deg, var(--teal) 0%, #ffffff 8%, var(--navy) 14%, var(--navy) 45%, var(--teal) 55%, var(--teal) 100%);
  }
  .brush-coral {
    left: 230px;
    top: 74px;
    width: 70px;
    height: 632px;
    background: linear-gradient(180deg, var(--coral) 0%, #ffffff 8%, var(--navy) 14%, var(--navy) 45%, var(--coral) 55%, var(--coral) 100%);
  }
  .pack-title {
    position: absolute;
    left: 6px;
    top: 708px;
    transform-origin: top left;
    transform: rotate(-90deg);
    display: flex;
    align-items: center;
    gap: 8px;
    white-space: nowrap;
    font-family: "Poppins", sans-serif;
    color: var(--ink);
  }
  .pack-count {
    width: 64px;
    height: 64px;
    border-radius: 50%;
    background: var(--coral);
    color: var(--white);
    font-weight: 600;
    font-size: 44px;
    line-height: 64px;
    text-align: center;
  }
  .pack-name {
    font-weight: 600;
    font-size: 27px;
    line-height: 30px;
  }
  .pack-tagline {
    margin-left: 18px;
    font-weight: 300;
    font-size: 27px;
    line-height: 30px;
  }
</style>
</head>
<body>
<main class="canvas">
  <section class="blister-card">
    <svg class="card-swoosh" width="330" height="748" viewBox="0 0 330 748" aria-hidden="true">
      <path d="M330 80 C 200 90, 40 220, 18 420 C 8 560, 30 660, 60 748 L 150 748 C 210 640, 290 560, 330 500 Z" fill="#ffffff"/>
    </svg>
    <div class="hang-hole"></div>

    <div class="brand">
      <span class="brand-dot"></span>
      <span class="brand-name">Brightwave</span>
    </div>

    <div class="product tongue-cleaner" role="img" aria-label="Purple tongue cleaner illustration"></div>
    <div class="product brush-teal" role="img" aria-label="Teal and navy toothbrush illustration"></div>
    <div class="product brush-coral" role="img" aria-label="Coral red and navy toothbrush illustration"></div>

    <div class="pack-title">
      <div class="pack-count">3</div>
      <div class="pack-name">Fresh<br>Package</div>
      <div class="pack-tagline">comfortable<br>toothbruhs</div>
    </div>
  </section>
</main>
</body>
</html>
```